Modern Business Card Design for Independent Urban Music Label

We need a card design for an independent urban music label called Copper Tide Records based in London. We develop and promote urban British music artists. We attend lots of high profile events with high profile industry people and want a card that comes across both on-brand and sophisticated, professional, trustworthy. I have attached our logo - please use the black and orange version in the upper left HOWEVER we are open to seeing other colors than the orange used though we want the shape of the logo to remain the same.

Info to please include:
Name
Position
Phone
Email
Website

Additional Info:
Twitter: @CopperTideRecsUK
Insta: @CopperTideRecs

Target Market(s)

Industry professionals and others artists

Industry/Entity Type

Business

Contact Information for Business Card

Info to please include:
Name
Position
Phone
Email
Website

Additional Info:
Twitter: @CopperTideRecsUK
Insta: @CopperTideRecs

Requirements
Must have
• Logo, company name
• Info to please include:
• Name
• Position
• Phone
• Email
• Website
Nice to have
• Twitter: @CopperTideRecsUK
• Insta: @CopperTideRecs
• If it can be done so that it doesn't look cluttered

```html
<!DOCTYPE html>
<html lang="en">
<head>
<meta charset="utf-8">
<title>Copper Tide Records – Business Card</title>
<link href="https://fonts.googleapis.com/css2?family=Encode+Sans+Condensed:wght@400;500&family=Open+Sans:wght@400;700&display=swap" rel="stylesheet">
<style>
  :root {
    --backdrop: #ebeceb;
    --card: #ffffff;
    --copper: #f29152;
    --copper-soft: #f6b58a;
    --ink: #2b2a29;
    --ink-text: #333333;
    --white: #ffffff;
  }
  html, body {
    margin: 0;
    padding: 0;
    width: 1200px;
    height: 966px;
    overflow: hidden;
    background: var(--backdrop);
  }
  .canvas {
    position: relative;
    width: 1200px;
    height: 966px;
  }
  .card {
    position: absolute;
    width: 437px;
    height: 693px;
    background: var(--card);
    overflow: hidden;
    box-shadow: 6px 8px 14px rgba(0, 0, 0, 0.18);
  }
  .card--front { left: 121px; top: 143px; }
  .card--back  { left: 606px; top: 141px; }

  /* Front */
  .front-glow {
    position: absolute;
    left: 0; right: 0;
    top: 160px;
    height: 311px;
    background: linear-gradient(to bottom, var(--card) 0%, var(--copper-soft) 55%, var(--copper) 85%, var(--copper) 100%);
  }
  .brand-mark {
    position: absolute;
    left: 50%;
    top: 255px;
    width: 124px;
    height: 124px;
    margin-left: -62px;
    border-radius: 50%;
    background: var(--ink);
  }
  .brand-name {
    position: absolute;
    left: 0; right: 0;
    top: 520px;
    text-align: center;
    font-family: "Encode Sans Condensed", sans-serif;
    font-weight: 500;
    font-size: 38px;
    letter-spacing: 2px;
    text-transform: uppercase;
    color: var(--copper);
    line-height: 1;
  }
  .footer-accent {
    position: absolute;
    left: 0; right: 0;
    top: 590px;
    bottom: 0;
    background: var(--copper);
    border-radius: 14px 14px 0 0;
  }
  .footer-band {
    position: absolute;
    left: 0; right: 0;
    top: 598px;
    bottom: 0;
    background: var(--ink);
    border-radius: 14px 14px 0 0;
  }
  .front-url {
    position: absolute;
    left: 0; right: 0;
    top: 622px;
    text-align: center;
    font-family: "Encode Sans Condensed", sans-serif;
    font-size: 28px;
    color: var(--white);
    line-height: 1.2;
  }

  /* Back */
  .back-glow {
    position: absolute;
    left: 0; right: 0;
    top: 0;
    height: 310px;
    background: linear-gradient(to bottom, var(--copper) 0%, var(--copper) 15%, var(--copper-soft) 55%, var(--card) 100%);
  }
  .holder {
    position: absolute;
    left: 58px;
    top: 297px;
    font-family: "Open Sans", sans-serif;
    color: var(--ink-text);
  }
  .holder__name {
    font-weight: 700;
    font-size: 24px;
    line-height: 1.3;
    margin: 0;
  }
  .holder__role {
    font-size: 20px;
    line-height: 1.3;
    margin: 2px 0 0;
  }
  .contact-list {
    position: absolute;
    left: 57px;
    top: 391px;
    margin: 0;
    padding: 0;
    list-style: none;
    font-family: "Open Sans", sans-serif;
    font-size: 22px;
    color: var(--ink-text);
  }
  .contact-list li {
    display: flex;
    align-items: center;
    height: 40.5px;
  }
  .contact-list svg {
    width: 22px;
    height: 22px;
    margin-right: 12px;
    flex: none;
  }
  .back .footer-accent { top: 589px; }
  .back .footer-band { top: 597px; }
  .social-list {
    position: absolute;
    left: 99px;
    top: 613px;
    margin: 0;
    padding: 0;
    list-style: none;
    font-family: "Open Sans", sans-serif;
    font-size: 22px;
    color: var(--white);
  }
  .social-list li {
    display: flex;
    align-items: center;
    height: 34px;
  }
  .social-dot {
    width: 22px;
    height: 22px;
    background: var(--copper);
    margin-right: 16px;
    flex: none;
  }
</style>
</head>
<body>
<div class="canvas">

  <section class="card card--front">
    <div class="front-glow"></div>
    <div class="brand-mark"></div>
    <div class="brand-name">Copper Tide Records</div>
    <div class="footer-accent"></div>
    <div class="footer-band"></div>
    <div class="front-url">www.CopperTideRecords.co.uk</div>
  </section>

  <section class="card card--back back">
    <div class="back-glow"></div>

    <div class="holder">
      <p class="holder__name">Your Name</p>
      <p class="holder__role">Position</p>
    </div>

    <ul class="contact-list">
      <li>
        <svg viewBox="0 0 22 22" aria-hidden="true"><path d="M5 2 L8 2 L9.5 7 L7.5 8.5 Q9 13 13.5 14.5 L15 12.5 L20 14 L20 17 Q19 20 15.5 19.5 Q5 17 2.5 6.5 Q2 3 5 2 Z" fill="none" stroke="var(--copper)" stroke-width="1.8" stroke-linejoin="round"/></svg>
        <span>123-456-7890</span>
      </li>
      <li>
        <svg viewBox="0 0 22 22" aria-hidden="true"><rect x="4" y="1.5" width="14" height="19" rx="2" fill="none" stroke="var(--copper)" stroke-width="1.8"/><line x1="9" y1="17" x2="13" y2="17" stroke="var(--copper)" stroke-width="1.8"/></svg>
        <span>123-456-7888</span>
      </li>
      <li>
        <svg viewBox="0 0 22 22" aria-hidden="true"><rect x="1.5" y="5" width="19" height="13" fill="none" stroke="var(--copper)" stroke-width="1.6"/><path d="M1.5 5 L11 12.5 L20.5 5" fill="none" stroke="var(--copper)" stroke-width="1.6"/></svg>
        <span>name@coppertiderecords.co.uk</span>
      </li>
      <li>
        <svg viewBox="0 0 22 22" aria-hidden="true"><g fill="none" stroke="var(--copper)" stroke-width="1.5"><circle cx="11" cy="11" r="9.5"/><ellipse cx="11" cy="11" rx="4.5" ry="9.5"/><line x1="1.5" y1="11" x2="20.5" y2="11"/><line x1="11" y1="1.5" x2="11" y2="20.5"/></g></svg>
        <span>www.coppertiderecords.co.uk</span>
      </li>
    </ul>

    <div class="footer-accent"></div>
    <div class="footer-band"></div>
    <ul class="social-list">
      <li><span class="social-dot"></span><span>@CopperTideRecsUK</span></li>
      <li><span class="social-dot"></span><span>@CopperTideRecs</span></li>
    </ul>
  </section>

</div>
</body>
</html>
```